A website for a Maltese Law Firm

Our law firm needs a website to further its business. The site should have a simple yet effective design. We would need the following sections: About us, Practice Areas, About Malta, Contact. These should be further split as follows:

About us: Our firm, Our values, What others say, Offices

Practice Areas: Crimimal, Citizenship & Residence, Harbour Passage Scheme, Criminal Defence, Civil Litigation, Arbitration and ADR, Commercial and Corporate, Media Law.

About Malta: just one section.

Contact: Just one section

We would also need a news feed at the front of the site to include latest news regarding our cases.

At the bottom we need a section for our Terms and a Privacy Statement.

Our logo is being attached.

Target Market(s)

All clients looking for legal assistance in Malta

Industry/Entity Type

Legal

Coding

Coded - Design and coding required

Number of Pages Required

1 page

Requirements
Must have
• It must be simple yet striking.

```html
<!DOCTYPE html>
<html lang="en">
<head>
<meta charset="utf-8">
<title>Galea &amp; Mifsud Advocates</title>
<link rel="stylesheet" href="https://fonts.googleapis.com/css2?family=Cinzel:wght@400;700&family=Raleway:wght@400;600&display=swap">
<style>
:root{
  --ink:#2b2b2b;
  --text:#6a6a6a;
  --line:#cfcfcf;
  --paper:#ffffff;
  --mist:#efefef;
  --footer:#333333;
  --footer-text:#c9c9c9;
  --input:#4a4a4a;
}
*{box-sizing:border-box;margin:0;padding:0}
html,body{width:1200px;height:2397px;overflow:hidden}
body{background:var(--paper);font-family:'Raleway',sans-serif;color:var(--text);position:relative}
.abs{position:absolute}

/* top bar */
.topbar{position:absolute;top:0;left:0;width:1200px;height:35px;border-bottom:1px solid #e3e3e3}
.social-top{position:absolute;left:99px;top:0;display:flex}
.social-top span{width:35px;height:35px;border-right:1px solid #e3e3e3;display:flex;align-items:center;justify-content:center}
.social-top span:first-child{border-left:1px solid #e3e3e3}
.social-top i{width:8px;height:8px;border-radius:50%;background:#555;display:block}
.callbar{position:absolute;right:99px;top:0;width:221px;height:35px;background:var(--ink);color:#fff;font-family:'Cinzel',serif;font-size:12px;letter-spacing:1px;display:flex;align-items:center;justify-content:center;gap:10px}
.callbar svg{width:14px;height:14px}

/* header */
.header{position:absolute;top:35px;left:0;width:1200px;height:78px;border-bottom:2px solid var(--ink)}
.brand{position:absolute;left:99px;top:26px;font-family:'Raleway',sans-serif;font-weight:600;font-size:24px;line-height:28px;color:var(--ink)}
.nav{position:absolute;right:99px;top:30px;display:flex;gap:36px;font-family:'Cinzel',serif;font-size:14px;color:var(--ink)}
.nav .active{border-bottom:2px solid var(--ink);padding-bottom:4px}

/* hero */
.hero{position:absolute;top:115px;left:0;width:1200px;height:463px;
  background:linear-gradient(90deg,#f2f2f0 0%,#ebe9e4 35%,#c9c6c1 55%,#5f6570 75%,#3e4450 100%)}
.hero-title{position:absolute;left:100px;top:188px;font-family:'Cinzel',serif;font-weight:400;font-size:26px;line-height:34px;color:var(--ink)}
.hero-btn{position:absolute;left:100px;top:274px;width:228px;height:36px;border:1px solid var(--ink);font-family:'Cinzel',serif;font-size:12px;letter-spacing:1px;color:var(--ink);display:flex;align-items:center;justify-content:center}
.hero-arrow{position:absolute;top:195px;width:48px;height:48px}

/* headings */
.sec-title{font-family:'Cinzel',serif;font-weight:400;font-size:26px;color:#6a6a6a;letter-spacing:.5px}
.sec-title b{font-weight:400;color:var(--ink);border-bottom:2px solid var(--ink);padding:0 2px 2px;border-top:1px solid var(--ink)}
.center{width:1200px;text-align:center;left:0}

.body-copy{font-size:13px;line-height:25.6px;color:var(--text)}
.btn-dark{background:var(--ink);color:#fff;font-family:'Cinzel',serif;font-size:13px;letter-spacing:1px;display:flex;align-items:center;justify-content:center}
.btn-line{border:1px solid var(--ink);color:var(--ink);font-family:'Cinzel',serif;font-size:12px;letter-spacing:1px;display:flex;align-items:center;justify-content:center}

/* about */
.about{position:absolute;top:578px;left:0;width:1200px;height:368px}
.value{position:absolute;left:748px;width:353px}
.value-icon{position:absolute;left:0;top:0;width:96px;height:96px;border:1px solid var(--line);display:flex;align-items:center;justify-content:center}
.value-icon svg{width:60px;height:50px}
.value h3{position:absolute;left:115px;top:6px;font-family:'Cinzel',serif;font-weight:400;font-size:17px;color:var(--ink)}
.value p{position:absolute;left:115px;top:34px;width:240px;font-size:12px;line-height:19px;color:#8a8a8a}

/* practice */
.practice{position:absolute;top:946px;left:0;width:1200px;height:350px;background:linear-gradient(180deg,#efefef,#eaeaea)}
.area{position:absolute;top:117px;width:152px}
.area-box{width:152px;height:96px;border:1px solid #d4d4d4;background:#f3f3f3;display:flex;align-items:center;justify-content:center}
.area-box svg{width:58px;height:54px}
.area-label{height:55px;border-bottom:1px solid #9a9a9a;font-family:'Cinzel',serif;font-size:13px;color:var(--ink);text-align:center;line-height:14px;display:flex;align-items:center;justify-content:center;letter-spacing:.5px}
.dots{position:absolute;top:297px;left:580px;display:flex;gap:4px}
.dots i{width:9px;height:9px;border:1px solid #888;border-radius:50%;display:block}
.dots i.on{background:#888;box-shadow:inset 0 0 0 2px #efefef}

/* malta */
.malta{position:absolute;top:1296px;left:0;width:1200px;height:424px}
.malta-frame{position:absolute;left:99px;top:105px;width:422px;height:248px;border:1px solid var(--line)}
.malta-photo{position:absolute;left:117px;top:123px;width:420px;height:248px;
  background:linear-gradient(180deg,#5d8fc7 0%,#9fb8d6 35%,#d7a865 55%,#6d7fb5 70%,#3f68b0 100%)}
.ticks{position:absolute;left:566px;top:268px;width:535px;list-style:none}
.ticks li{position:relative;padding-left:22px;font-size:13px;line-height:17px;font-weight:600;color:var(--ink);margin-bottom:15px}
.ticks svg{position:absolute;left:0;top:2px;width:13px;height:13px}

/* news */
.news{position:absolute;top:1720px;left:0;width:1200px;height:455px;background:linear-gradient(90deg,#e9ecf2,#dfe4ee 60%,#e8ebf1)}
.story{position:absolute;top:116px;width:480px}
.story-photo{width:480px;height:172px;position:relative}
.photo-reader{background:linear-gradient(90deg,#1c1e22,#4a4c52 50%,#1f2024)}
.photo-gavel{background:linear-gradient(90deg,#e6e2dc,#c9bfae 40%,#7a4a24 70%,#d8d4cf)}
.date{position:absolute;left:0;bottom:0;width:61px;height:59px;background:var(--ink);color:#fff;text-align:center;font-size:20px;line-height:22px;padding-top:8px;font-weight:600}
.date small{display:block;font-size:12px;font-weight:400;letter-spacing:1px}
.story p{margin-top:17px;font-size:12.5px;line-height:24px;color:var(--text)}
.story .btn-line{position:absolute;top:255px;width:126px;height:36px}

/* footer */
.footer{position:absolute;top:2175px;left:0;width:1200px;height:222px;background:var(--footer);color:var(--footer-text)}
.f-brand{position:absolute;left:122px;top:86px;font-family:'Raleway',sans-serif;font-weight:600;font-size:21px;line-height:26px;color:#fff}
.copy{position:absolute;left:99px;top:140px;font-size:11px}
.f-head{position:absolute;top:44px;font-family:'Cinzel',serif;font-size:16px;color:#fff;letter-spacing:1.5px;border-bottom:1px solid #777;padding-bottom:6px}
.f-link{position:absolute;font-size:11px;padding-left:16px}
.f-link::before{content:"";position:absolute;left:0;top:3px;width:6px;height:6px;border:1px solid #aaa;transform:rotate(45deg)}
.f-social{position:absolute;left:592px;top:171px;display:flex;gap:14px}
.f-social i{width:10px;height:10px;background:#fff;border-radius:50%;display:block}
.newsletter{position:absolute;left:800px;top:94px;width:301px;height:34px;display:flex}
.newsletter .field{flex:1;background:var(--input);font-size:11px;font-style:italic;color:#bbb;display:flex;align-items:center;padding-left:14px}
.newsletter .send{width:45px;background:#cfcfcf;display:flex;align-items:center;justify-content:center}
.f-contact{position:absolute;font-size:11px;display:flex;align-items:center;gap:8px}
.f-contact svg{width:11px;height:11px}
</style>
</head>
<body>

<div class="topbar">
  <div class="social-top"><span><i></i></span><span><i></i></span><span><i></i></span><span><i></i></span></div>
  <div class="callbar">
    <svg viewBox="0 0 16 16"><circle cx="8" cy="8" r="7.5" fill="#555"/><path d="M5 4l2 2-1 1.2c.6 1.2 1.6 2.2 2.8 2.8L10 9l2 2-1.4 1.4C7.5 12 4 8.5 3.6 5.4z" fill="#fff"/></svg>
    CALL US : (000) 0000 0000
  </div>
</div>

<header class="header">
  <div class="brand">Galea &amp; Mifsud</div>
  <nav class="nav"><span class="active">Home</span><span>About Us</span><span>Practice Areas</span><span>About Malta</span><span>Contact</span></nav>
</header>

<section class="hero" role="img" aria-label="Photo of two advocates in suits reviewing a tablet at an office desk">
  <svg class="hero-arrow" style="left:27px" viewBox="0 0 48 48"><path d="M18 4H8a4 4 0 0 0-4 4v32a4 4 0 0 0 4 4h10" fill="none" stroke="#2b2b2b" stroke-width="2"/><path d="M40 24H14M22 16l-8 8 8 8" fill="none" stroke="#2b2b2b" stroke-width="2"/></svg>
  <svg class="hero-arrow" style="left:1128px" viewBox="0 0 48 48"><path d="M30 4h10a4 4 0 0 1 4 4v32a4 4 0 0 1-4 4H30" fill="none" stroke="#ddd" stroke-width="2"/><path d="M8 24h26M26 16l8 8-8 8" fill="none" stroke="#ddd" stroke-width="2"/></svg>
  <h1 class="hero-title">The Greatest &amp; Stongest<br>Firm You Can Trust</h1>
  <div class="hero-btn">Request A Free Consultant</div>
</section>

<section class="about">
  <h2 class="sec-title abs" style="left:99px;top:62px">About <b>Galea &amp; Mifsud</b></h2>
  <p class="body-copy abs" style="left:99px;top:108px;width:592px">Lorem ipsum dolor sit amet, consectetuer adipiscing elit, sed diam nonummy nibh euismod tincidunt ut laoreet dolore magna aliquam erat volutpat. Ut wisi enim ad minim veniam, quis nostrud exerci tation ullamcorper suscipit lobortis nisl ut aliquip ex ea commodo consequat. Duis autem vel eum iriure dolor in hendrerit in vulputate velit esse molestie consequat, vel illum dolore eu feugiat nulla facilisis at vero eros et accumsan et iusto odio dignissim qui blandit praesent luptatum te feugait nulla facilisi.</p>
  <div class="btn-dark abs" style="left:99px;top:278px;width:134px;height:39px">Read More</div>

  <div class="value" style="top:86px">
    <div class="value-icon"><svg viewBox="0 0 60 50"><path d="M2 18l10-6 8 3 8-4h8l10 4 8-4 4 12-8 4-10 12-6 4-6-4-8-8-8-6z" fill="#2b2b2b"/><path d="M22 26l6 6M26 22l6 6M30 18l6 6" stroke="#fff" stroke-width="2"/></svg></div>
    <h3>Our Values</h3>
    <p>Artis nisl ut aliquip ex ea commodoll eros et accumsan o digniss qui nulla facilisi...[+]</p>
  </div>
  <div class="value" style="top:213px">
    <div class="value-icon"><svg viewBox="0 0 60 50"><path d="M30 4L6 16h48z" fill="#2b2b2b"/><rect x="8" y="18" width="44" height="3" fill="#2b2b2b"/><rect x="12" y="23" width="5" height="16" fill="#2b2b2b"/><rect x="22" y="23" width="5" height="16" fill="#2b2b2b"/><rect x="33" y="23" width="5" height="16" fill="#2b2b2b"/><rect x="43" y="23" width="5" height="16" fill="#2b2b2b"/><rect x="6" y="41" width="48" height="4" fill="#2b2b2b"/></svg></div>
    <h3>Our Firm</h3>
    <p>Artis nisl ut aliquip ex ea commodoll eros et accumsan o digniss qui nulla facilisi...[+]</p>
  </div>
</section>

<section class="practice">
  <h2 class="sec-title abs center" style="top:46px">Practice <b>Areas</b></h2>
  <div class="area" style="left:99px">
    <div class="area-box"><svg viewBox="0 0 58 54"><circle cx="17" cy="34" r="11" fill="none" stroke="#2b2b2b" stroke-width="4"/><circle cx="41" cy="30" r="11" fill="none" stroke="#2b2b2b" stroke-width="4"/><rect x="12" y="14" width="10" height="8" rx="2" fill="#2b2b2b"/><rect x="36" y="10" width="10" height="8" rx="2" fill="#2b2b2b"/><path d="M22 18h14" stroke="#2b2b2b" stroke-width="3"/></svg></div>
    <div class="area-label">Criminal Law</div>
  </div>
  <div class="area" style="left:311px">
    <div class="area-box"><svg viewBox="0 0 58 54"><path d="M29 6L4 28h7v20h14V36h8v12h14V28h7z" fill="#2b2b2b"/></svg></div>
    <div class="area-label">Citizenship &amp;<br>Residence</div>
  </div>
  <div class="area" style="left:524px">
    <div class="area-box"><svg viewBox="0 0 58 54"><rect x="12" y="6" width="34" height="42" rx="2" fill="none" stroke="#2b2b2b" stroke-width="3"/><circle cx="29" cy="22" r="8" fill="none" stroke="#2b2b2b" stroke-width="3"/><path d="M18 38h22M18 43h16" stroke="#2b2b2b" stroke-width="3"/></svg></div>
    <div class="area-label">Harbour Passage<br>Scheme</div>
  </div>
  <div class="area" style="left:736px">
    <div class="area-box"><svg viewBox="0 0 58 54"><rect x="14" y="10" width="22" height="10" rx="2" transform="rotate(35 25 15)" fill="#2b2b2b"/><path d="M28 22l16 14" stroke="#2b2b2b" stroke-width="4"/><rect x="8" y="42" width="28" height="6" fill="#2b2b2b"/></svg></div>
    <div class="area-label">Civil<br>Litigation</div>
  </div>
  <div class="area" style="left:949px">
    <div class="area-box"><svg viewBox="0 0 58 54"><rect x="14" y="6" width="30" height="26" rx="2" fill="#2b2b2b"/><rect x="19" y="11" width="20" height="16" fill="#f3f3f3"/><rect x="6" y="36" width="46" height="4" fill="#2b2b2b"/><rect x="10" y="43" width="38" height="4" fill="#2b2b2b"/></svg></div>
    <div class="area-label">Arbitration<br>and ADR</div>
  </div>
  <div class="dots"><i class="on"></i><i></i><i></i></div>
</section>

<section class="malta">
  <h2 class="sec-title abs center" style="top:44px">About <b>Malta</b></h2>
  <div class="malta-frame"></div>
  <div class="malta-photo" role="img" aria-label="Photo of a harbour city skyline at dusk"></div>
  <p class="body-copy abs" style="left:566px;top:106px;width:535px">Aeuismod tincidunt ut laoreet dolore magna aliquam erat volutpat. Ut wisi enim ad minim veniam, quis nostrud exerci tation ullamcorper suscipit lobortis nisl ut aliquip ex ea commodo consequat. Duis autem vel eum iriure dolor in hendrerit in vulputate velit esse molestie consequat, vel illum dolore eu feugiat nulla facilisis at vero eros et accumsan et iusto odio dignissim qui blandit praesent luptatum te feugait nulla facilisi.</p>
  <ul class="ticks">
    <li><svg viewBox="0 0 13 13"><path d="M1 4h6V1l5 5.5L7 12V9H1z" fill="none" stroke="#2b2b2b"/></svg>Duis autem vel eum iriure dolor in hendrerit in vulputate vl conseqt,molestie consequat vel illum dolore.</li>
    <li><svg viewBox="0 0 13 13"><path d="M1 4h6V1l5 5.5L7 12V9H1z" fill="none" stroke="#2b2b2b"/></svg>Ut wisi enim ad minim veniam, qui nostrud exeullamcorper suscipit lobortis .</li>
    <li><svg viewBox="0 0 13 13"><path d="M1 4h6V1l5 5.5L7 12V9H1z" fill="none" stroke="#2b2b2b"/></svg>Aulputate velit esse molestie consequat, vel illum dolore eu feugiat.</li>
  </ul>
</section>

<section class="news">
  <h2 class="sec-title abs center" style="top:46px">Latest <b>News</b></h2>
  <article class="story" style="left:99px">
    <div class="story-photo photo-reader" role="img" aria-label="Photo of a man studying case papers at a desk"><div class="date">08<small>JUNE</small></div></div>
    <p>lobortis nisl ut aliquip ex ea commodo consequat. Duis autem vel eum iriure dolor in hendrerit inilore eu feugiat nulla facilisis at vero..</p>
    <div class="btn-line">Read More</div>
  </article>
  <article class="story" style="left:622px">
    <div class="story-photo photo-gavel" role="img" aria-label="Photo of a wooden gavel resting on an open law book"><div class="date">08<small>JUNE</small></div></div>
    <p>lobortis nisl ut aliquip ex ea commodo consequat. Duis autem vel eum iriure dolor in hendrerit in vulpue molestie ct, velo..</p>
    <div class="btn-line">Read More</div>
  </article>
</section>

<footer class="footer">
  <div class="f-brand">Galea &amp; Mifsud</div>
  <div class="copy">Copyright © 2016 GMadvocates. All rights reserved.</div>

  <div class="f-head" style="left:466px">Navigation</div>
  <div class="f-link" style="left:462px;top:92px">Home</div>
  <div class="f-link" style="left:462px;top:132px">About us</div>
  <div class="f-link" style="left:462px;top:171px">Practice Areas</div>
  <div class="f-link" style="left:590px;top:92px">About Malta</div>
  <div class="f-link" style="left:590px;top:132px">Contact Us</div>
  <div class="f-social"><i></i><i></i><i></i><i></i></div>

  <div class="f-head" style="left:800px">Newsletter</div>
  <div class="newsletter"><div class="field">Enter Your Email</div><div class="send"><svg width="18" height="16" viewBox="0 0 18 16"><path d="M1 7L17 1 13 15 8 10z M8 10l9-9" fill="none" stroke="#333" stroke-width="1.4"/></svg></div></div>
  <div class="f-contact" style="left:808px;top:147px"><svg viewBox="0 0 11 11"><path d="M5.5 0a4 4 0 0 0-4 4c0 3 4 7 4 7s4-4 4-7a4 4 0 0 0-4-4z" fill="#fff"/><circle cx="5.5" cy="4" r="1.4" fill="#333"/></svg>00 Sample Street, Exampletown</div>
  <div class="f-contact" style="left:808px;top:174px"><svg viewBox="0 0 11 11"><path d="M2 0l2 2.5-1 1.2c.7 1.5 2 2.8 3.4 3.4l1.2-1L10 8 8.6 10.5C4.5 10 1 6.5.5 2.4z" fill="#fff"/></svg>(000) 0000 0000</div>
  <div class="f-contact" style="left:944px;top:174px"><svg viewBox="0 0 11 11"><rect x="0" y="2" width="11" height="7" fill="#fff"/><path d="M0 2l5.5 4L11 2" fill="none" stroke="#333"/></svg>info@gmadvocates.example</div>
</footer>

</body>
</html>
```